Can you make FairlyNeat look better than average? We need business cards and a logo refresh :-)

REVISED BRIEF

PRIORITY

VECTOR LOGO

Create a vector version of our existing logo. The logo must not change from its current design, weight or font.

Deliverables

- Logo in blue (#2540BB)
- Logo in white (#FFFFFF)
- Logo in grey (#36454F)
- All logos on transparent background
- All logos in PNG & SVG formats. (SVG must NOT distort stroke width when resized)

BRAND MARK

Create a brand mark for use with the logo. This should be possible to used with the logo and on its own as a stand alone graphical device that represents the FAIRLYNEAT brand.

https://quellbrik.com/resources/glossary/what-is-a-brand-mark

Deliverables

- Brand Mark in blue (#2540BB)
- Brand Mark in white (#FFFFFF)
- Brand Mark in grey (#36454F)
- Brand Mark on transparent background
- Brand Mark in PNG & SVG formats. (SVG must NOT distort stroke width when resized)
- Logo combined with Brand Mark (colours and formats)
.

Business Card Layout

Create 2 layouts with the following details:-

Marcus Delaney
Co-Founder & Chief Product Officer

marcus@fairlyneat.nz
www.fairlyneat.nz
0279831465

Callum Ferris
Founder & CEO

hello@fairlyneat.nz
www.fairlyneat.nz
021 684 2590

DESIGN CONSIDERATIONS

Create versions with ‘Shaping Causes With Heart’ tag line incorporated within the design and without (maintain separation of logo from tag line)

- Create a version with and without the brand mark
- Keep it clean and simple but elevate the design with subtle design effects
- Consider use of raised spot gloss colour (this can be white on white for subtle or blue on blue or blue on white)
- Consider use of spot gloss colour (this can be white on white for subtle or blue on blue or blue on white)
- Consider use of letterpress indentation
- Ensure contact details are legible, use sans-serif font

PREVIOUS BRIEF

We need a business card design for our business FairlyNeat. We are a purpose driven brand and media agency that helps brands and charities plan and buy traditional media campaigns (TV, Radio, Print, Outdoor etc). We give a significant amount of the media booking fees we receive from media vendors to charity in the name of our clients. https://www.plinkwork.com/posts/wearefairlyneat_giveback-fairlyneat-shapingcauseswithheart-activity-5829170364418205731-Rtqe

Our strapline is 'Shaping Causes With Heart'.

We want to keep our logo design as it is but it does need tightening up and made into a proper vector image as it's been created from a font.

Our brand colour is #2540BB and we need to keep this.

Our brand is professional but human, warm and engaging and doesn't take itself too seriously.

Things We Need
- vectorisation and tidying up of existing logo
- We'd like you to think about how we can incorporate a brand mark with the logo to add another dimension to our brand
- business card layout and design
- we'll be using zentiprint.com to print the cards so please take a look at the options they have (spot gloss, foil, letterpress, square cards and even the backs of the cards can have a different design on every single card!
- potential opportunity for different famous quotes on the back or imagery or slight design differences
- we'd be open to the use of an emoji or emojiis as the brandmark or to be incorporated into the card designs
- we can have as many different design batches as we like for the backs of the cards

https://www.zentiprint.com/au/business-cards

We want to make an impact, we want to be seen as professional but fun, we want to be different.

Here's a press release of what we're about.

https://adwirely.co.nz/movings-shakings/fairlyneat-welcomes-marcus-delaney-as-co-founder/

Be bold, be different, there is no such thing as a bad idea. We're open to anything so please bring your best ideas and have fun with it! Go crazy if you like!
____________
Marcus Delaney
marcus@fairlyneat.nz
0279831465

Callum Ferris
Founder & CEO
hello@fairlyneat.nz
021 684 2590

Shaping Causes With Heart

________

These are the only details we MUST have on the cards, the rest is up to you. Just make sure you use all of your creativity but don't feel the need to crowd the card with too much, let it breathe as well.

In terms of font for the details, we'll leave that up to you, just ensure it's legible. Oh and please don't take any design inspiration from our website - that will be changing!

Please don't let the design and layout look cheap and tacky though. It needs to still feel premium but personable.

Thanks

Marcus

Many designs are changing the logo and this was NOT in the brief. We need a brand mark to complement the logo. We need to see the logo with and without the brand mark. We need to see the business card with both logo + brand mark and logo on its own We need to see the business card with and without the tagline 'Shaping Causes With Heart'

purpose driven Brand & Media Agency

Shaping Causes With Heart
Marcus Delaney, Co-Founder & Chief Product Officer, marcus@fairlyneat.nz fairlyneet.nz, 0279 831 465

Callum Ferris, Founder & CEO hello@fairlyneat.nz, fairlyneet.nz, 021 684 2590

Serif
Sans Serif

0054AA
0677BA
7BADD7
CADEEF
E8F1F8

• brand mark, vector version of existing logo, Shaping Causes With Heart tagline, existing logo traced and vectorised. Must fully explore the design options from zentiprint.com that can enhance the overall card design
• brandmark to help elevate the logo, maybe incorporate some other design elements into the card like lines, or grids.
• A cheap look and feel

```html
<!DOCTYPE html>
<html lang="en">
<head>
<meta charset="utf-8">
<title>FairlyNeat Business Card</title>
<link href="https://fonts.googleapis.com/css2?family=Poppins:wght@400;500;600&display=swap" rel="stylesheet">
<style>
  :root {
    --brand: #3a4ea6;
    --paper: #ffffff;
    --stage: #e8e5e0;
  }
  html, body {
    margin: 0;
    padding: 0;
    width: 1189px;
    height: 1200px;
    overflow: hidden;
    background: var(--stage);
    font-family: "Poppins", sans-serif;
  }
  .canvas {
    position: relative;
    width: 1189px;
    height: 1200px;
  }
  .card {
    position: absolute;
    left: 223px;
    width: 744px;
    box-shadow: 0 6px 18px rgba(0,0,0,0.18);
  }
  .card--front {
    top: 111px;
    height: 486px;
    background: var(--paper);
  }
  .card--back {
    top: 640px;
    height: 488px;
    background: var(--brand);
  }
  .side-band {
    position: absolute;
    left: 0;
    top: 0;
    width: 178px;
    height: 100%;
    background: var(--brand);
  }
  .side-band svg,
  .back-logo {
    position: absolute;
    left: 0;
    top: 0;
  }
  .wordmark {
    font-family: "Poppins", sans-serif;
    font-weight: 600;
    fill: var(--paper);
  }
  .tagline {
    font-family: "Poppins", sans-serif;
    font-weight: 500;
    fill: var(--paper);
  }
  .contact {
    position: absolute;
    left: 255px;
    color: var(--brand);
  }
  .contact__name {
    margin: 0;
    font-size: 24px;
    font-weight: 600;
    letter-spacing: 0.5px;
    line-height: 1;
    text-transform: uppercase;
  }
  .contact__role {
    margin: 6px 0 0;
    font-size: 19px;
    font-weight: 400;
    letter-spacing: 1px;
    line-height: 1.1;
  }
  .contact__lines {
    list-style: none;
    margin: 22px 0 0;
    padding: 0;
    font-size: 19px;
    letter-spacing: 0.8px;
    line-height: 25px;
  }
  .contact__lines li {
    display: flex;
    align-items: center;
    gap: 12px;
  }
  .icon {
    width: 18px;
    height: 18px;
    fill: var(--brand);
    flex: none;
  }
  .contact--marcus { top: 107px; }
  .contact--callum { top: 279px; }
  .divider {
    position: absolute;
    left: 255px;
    top: 249px;
    width: 419px;
    height: 2px;
    background: var(--brand);
  }
</style>
</head>
<body>
<div class="canvas">

  <section class="card card--front">
    <div class="side-band">
      <svg width="178" height="486" viewBox="0 0 178 486">
        <text class="wordmark" x="0" y="0" font-size="58" text-anchor="middle"
              transform="translate(108 243) rotate(-90)">FairlyNeat</text>
      </svg>
    </div>

    <div class="contact contact--marcus">
      <h2 class="contact__name">Marcus Delaney</h2>
      <p class="contact__role">Co-Founder &amp; Chief Product Officer</p>
      <ul class="contact__lines">
        <li><svg class="icon" viewBox="0 0 24 24"><path d="M6.6 2.5c.6-.4 1.4-.2 1.8.4l1.7 3c.3.6.2 1.3-.3 1.7l-1.4 1c-.3.2-.4.6-.3.9.9 2.6 2.5 5.2 4.4 7.2.3.3.7.3 1 .1l1.3-.8c.6-.4 1.3-.2 1.7.3l1.9 2.8c.4.6.3 1.4-.3 1.8l-1.6 1.2c-.9.6-2.1.7-3 .1C8.8 19 5.3 13.6 4.6 7.6c-.1-1.1.3-2.2 1.1-2.9z"/></svg>0279831465</li>
        <li><svg class="icon" viewBox="0 0 24 24"><path d="M2 5h20v14H2z M3.5 6.5v.6l8.5 6 8.5-6v-.6z M3.5 8.9v8.6h17V8.9l-8.5 6z" fill-rule="evenodd"/></svg>marcus@fairlyneat.nz</li>
      </ul>
    </div>

    <div class="divider"></div>

    <div class="contact contact--callum">
      <h2 class="contact__name">Callum Ferris</h2>
      <p class="contact__role">Founder &amp; CEO</p>
      <ul class="contact__lines">
        <li><svg class="icon" viewBox="0 0 24 24"><path d="M6.6 2.5c.6-.4 1.4-.2 1.8.4l1.7 3c.3.6.2 1.3-.3 1.7l-1.4 1c-.3.2-.4.6-.3.9.9 2.6 2.5 5.2 4.4 7.2.3.3.7.3 1 .1l1.3-.8c.6-.4 1.3-.2 1.7.3l1.9 2.8c.4.6.3 1.4-.3 1.8l-1.6 1.2c-.9.6-2.1.7-3 .1C8.8 19 5.3 13.6 4.6 7.6c-.1-1.1.3-2.2 1.1-2.9z"/></svg>021 684 2590</li>
        <li><svg class="icon" viewBox="0 0 24 24"><path d="M2 5h20v14H2z M3.5 6.5v.6l8.5 6 8.5-6v-.6z M3.5 8.9v8.6h17V8.9l-8.5 6z" fill-rule="evenodd"/></svg>hello@fairlyneat.nz</li>
      </ul>
    </div>
  </section>

  <section class="card card--back">
    <svg class="back-logo" width="744" height="488" viewBox="0 0 744 488">
      <text class="wordmark" x="372" y="252" font-size="70" text-anchor="middle">FairlyNeat</text>
      <text class="tagline" x="372" y="288" font-size="18" text-anchor="middle" letter-spacing="6">SHAPING CAUSES WITH HEART</text>
    </svg>
  </section>

</div>
</body>
</html>
```